Flyer: Steady Steps, Bright Days

Please create a two (2) page flyer. We welcome minor updates/ changes to the Steady Steps Bright Days flyer that is attached as a word document. We are aiming for the same general look and feel as the original PDF attached (please note that we have updated the content and would like the designers to use what is listed in the word document).
We encourage you to provide multiple versions using pictures of different people we have on hand. Our team currently likes how the lady in the picture is looking in the direction of the text - we encourage designers to please flip the photo if needed to make this possible. We also give the permission to crop the photos as needed to fit the design better aesthetically. In addition, the team wondered about having a pdf file that allows the user to easily change out the graphic between different photos to reflect different communities best—not sure if that is as easy as it sounds. Please remember to include the funding statement - you can find it within both of the current documents. For more information about our project, please visit https://novelmarrow.org/wellness-path/

```html
<!DOCTYPE html>
<html lang="en">
<head>
<meta charset="utf-8">
<title>Steady Steps, Bright Days – Two-Page Flyer</title>
<link rel="stylesheet" href="https://fonts.googleapis.com/css2?family=Open+Sans:wght@600;700&family=Roboto+Condensed:ital,wght@0,400;0,700;1,400&family=Arimo:wght@400;700&display=swap">
<style>
:root{
  --stage:#6f7072;
  --paper:#fcf3ec;
  --maroon:#98483f;
  --red:#9c1e22;
  --rust:#a33a33;
  --teal:#4ba5aa;
  --ink:#2b2323;
  --pattern:#eddcd2;
}
*{box-sizing:border-box;margin:0;padding:0}
html,body{width:1200px;height:793px;overflow:hidden;background:var(--stage)}
body{position:relative;font-family:"Roboto Condensed",Arial,sans-serif;color:var(--ink)}
.page{position:absolute;top:84px;width:490px;height:635px;background:var(--paper);overflow:hidden}
.page--front{left:75px}
.page--back{left:626px}

/* FRONT */
.title-band{position:absolute;left:0;top:0;width:100%;height:74px;background:var(--maroon)}
.title-band h1{position:absolute;left:32px;top:18px;font-family:"Open Sans",sans-serif;font-weight:700;font-size:29px;color:#fff;letter-spacing:-.2px;white-space:nowrap}
.trim-band{position:absolute;left:0;top:74px;width:100%;height:16px;background:linear-gradient(#e2ccc2 0 45%,#8fb9bb 45% 60%,#e2ccc2 60%)}
.backdrop{position:absolute;left:0;top:90px;width:100%;height:510px;background:linear-gradient(90deg,var(--pattern),#f7e9e1 60%,var(--paper))}
.front-photo{position:absolute;left:0;top:100px;width:240px;height:500px;background:radial-gradient(ellipse at 45% 35%,#a46f5e 0,#c4a59a 35%,#d7a0a3 60%,rgba(252,243,236,0) 80%)}
.kicker{position:absolute;right:20px;font-family:"Arimo",Arial,sans-serif;font-size:12.4px;line-height:14px;color:var(--red);text-align:right;white-space:nowrap;font-weight:400}
.kicker--top{top:124px}
.intro{position:absolute;right:20px;top:162px;width:250px;font-size:8.6px;line-height:10.3px;text-align:justify;text-align-last:right}
.stats{position:absolute;right:20px;top:219px;width:250px;height:52px}
.stat{position:absolute;top:0;text-align:right}
.stat__icon{position:absolute;background:var(--maroon)}
.stat__num{font-family:"Open Sans",sans-serif;font-weight:600;font-size:22px;line-height:25px;color:var(--maroon);border-bottom:1px solid var(--maroon)}
.stat__cap{font-size:6.8px;line-height:7.8px;margin-top:2px}
.kicker--risk{top:282px}
.risk-list{position:absolute;right:20px;top:314px;list-style:none;font-size:11px;line-height:17px}
.risk-list li{display:flex;justify-content:flex-end;align-items:center;gap:5px;white-space:nowrap}
.check{width:10px;height:10px}
.pill{position:absolute;background:var(--teal);color:#fff;font-family:"Arimo",Arial,sans-serif;border-radius:12px;white-space:nowrap}
.pill--protect{right:20px;top:372px;width:232px;height:23px;font-size:8.4px;line-height:23px;text-align:center}
.protect-list{position:absolute;right:20px;top:403px;width:250px;list-style:none;font-size:8.1px;line-height:8.9px}
.protect-list li{display:flex;justify-content:flex-end;gap:6px;margin-bottom:4.2px;text-align:right}
.protect-list li span{display:block;white-space:nowrap}
.dot{flex:none;width:6px;height:6px;border-radius:50%;background:#d38d86;margin-top:1.5px}
.closing{position:absolute;right:32px;top:577px;font-style:italic;font-size:8px;line-height:9.6px;color:var(--red);text-align:right;white-space:nowrap}
.foot{position:absolute;left:0;top:600px;width:100%;height:35px;background:var(--maroon);color:#fff}
.foot--front p{font-size:9.4px;line-height:35px;padding-left:98px;white-space:nowrap}
.foot--front b{font-weight:700}

/* BACK */
.back-title{position:absolute;left:16px;top:26px;font-family:"Arimo",Arial,sans-serif;font-weight:700;font-size:12.6px;line-height:17.5px;color:var(--rust);white-space:nowrap}
.back-rule{position:absolute;left:16px;top:64px;width:148px;height:4px;background:var(--maroon)}
.back-intro{position:absolute;left:16px;top:74px;width:252px;font-size:8.6px;line-height:10.4px}
.back-intro p+p{margin-top:9px}
.portrait{position:absolute;border-radius:46% 40% 44% 50%}
.portrait--top{left:290px;top:0;width:200px;height:200px;background:radial-gradient(ellipse at 55% 45%,#b9826c 0,#d6bdb4 45%,rgba(252,243,236,0) 72%)}
.portrait--mid{left:310px;top:168px;width:180px;height:180px;background:radial-gradient(ellipse at 50% 45%,#8e5a45 0,#c99a8c 45%,rgba(252,243,236,0) 72%)}
.portrait--low{left:300px;top:305px;width:190px;height:230px;background:radial-gradient(ellipse at 55% 40%,#9c6a56 0,#cf7f70 40%,#a8bdd1 58%,rgba(252,243,236,0) 74%)}
.ribbon{position:absolute;left:0;top:167px;width:205px;height:22px;background:var(--maroon);clip-path:polygon(0 0,100% 0,95% 100%,0 100%);color:#fff;font-family:"Arimo",Arial,sans-serif;font-size:10px;line-height:22px;padding-left:16px;white-space:nowrap}
.doctor-steps{position:absolute;left:16px;top:195px;width:300px;list-style:none}
.doctor-steps>li{position:relative;padding-left:27px;font-size:7px;line-height:8.3px;margin-bottom:5.6px}
.step-icon{position:absolute;left:0;top:0;width:19px;height:19px}
.lead{color:var(--red)}
.lead b{font-weight:700}
.doctor-steps ul{list-style:none;margin-top:1px;padding-left:4px}
.doctor-steps ul li::before{content:"•";margin-right:4px}
.pill--other{left:12px;top:448px;width:202px;height:22px;font-size:10px;line-height:22px;padding-left:10px;border-radius:0 11px 11px 0}
.other-steps{position:absolute;left:24px;top:475px;width:320px;list-style:none;font-size:7px;line-height:7.6px}
.other-steps li{position:relative;padding-left:15px;margin-bottom:2.3px}
.other-steps li::before{content:"";position:absolute;left:0;top:1px;width:5px;height:5px;border-radius:50%;border:1px solid var(--maroon)}
.org{position:absolute;left:352px;top:566px;display:flex;align-items:center;gap:6px}
.org__mark{width:18px;height:18px;background:var(--teal)}
.org__name{font-size:9px;line-height:10px;color:var(--teal);width:100px}
.foot--back p{font-size:6.2px;line-height:7.4px;padding:5px 16px 0}
</style>
</head>
<body>

<section class="page page--front" aria-label="Flyer page one">
  <header class="title-band"><h1>Steady Steps, Bright Days…</h1></header>
  <div class="trim-band" role="img" aria-label="Woven geometric trim band"></div>
  <div class="backdrop" role="img" aria-label="Soft woven geometric pattern backdrop"></div>
  <div class="front-photo" role="img" aria-label="Photo of an elder woman with white hair and a floral blouse, facing the text"></div>

  <h2 class="kicker kicker--top">KEEP YOUR HEART AND BODY HEALTHY<br>TO PROTECT YOUR BRAIN</h2>
  <p class="intro">Everyone slows down as they get older, both in body and mind. Big changes in memory or thinking that make it hard to get through the day are not a normal part of aging. These changes could be signs of early dementia or Alzheimer’s disease.</p>

  <div class="stats">
    <div class="stat__icon" role="img" aria-label="Map of the United States" style="left:0;top:8px;width:52px;height:30px;border-radius:6px 10px 14px 4px"></div>
    <div class="stat" style="left:56px;width:82px">
      <div class="stat__num">1 in 9</div>
      <p class="stat__cap">People in the U.S.<br>ages 65+ has<br>Alzheimer’s dementia</p>
    </div>
    <div class="stat__icon" role="img" aria-label="Group of people figures" style="left:148px;top:4px;width:36px;height:38px;border-radius:50% 50% 4px 4px"></div>
    <div class="stat" style="right:0;width:62px">
      <div class="stat__num">1 in 3</div>
      <p class="stat__cap">American Indian<br>people ages 65+<br>develops dementia</p>
    </div>
  </div>

  <h2 class="kicker kicker--risk">YOU ARE MORE AT RISK OF DEVELOPING<br>DEMENTIA IF YOU HAVE:</h2>
  <ul class="risk-list">
    <li>High Blood Pressure <svg class="check" viewBox="0 0 10 10"><circle cx="5" cy="5" r="4.3" fill="none" stroke="#98483f"/><path d="M3 5.2l1.5 1.5L7.2 3.8" fill="none" stroke="#98483f"/></svg></li>
    <li>Diabetes or <svg class="check" viewBox="0 0 10 10"><circle cx="5" cy="5" r="4.3" fill="none" stroke="#98483f"/><path d="M3 5.2l1.5 1.5L7.2 3.8" fill="none" stroke="#98483f"/></svg></li>
    <li>You Smoke Cigarettes <svg class="check" viewBox="0 0 10 10"><circle cx="5" cy="5" r="4.3" fill="none" stroke="#98483f"/><path d="M3 5.2l1.5 1.5L7.2 3.8" fill="none" stroke="#98483f"/></svg></li>
  </ul>

  <div class="pill pill--protect">YOU CAN PROTECT YOUR BODY, HEART, AND MIND</div>
  <ul class="protect-list">
    <li><span>Schedule a “wellness” visit and health screenings<br>every year with your doctor, even if you feel ok</span><i class="dot"></i></li>
    <li><span>Keep a healthy blood pressure</span><i class="dot"></i></li>
    <li><span>Be active or walk every day</span><i class="dot"></i></li>
    <li><span>Maintain a healthy weight for your body size</span><i class="dot"></i></li>
    <li><span>Eat a healthier diet with more fresh vegetables,<br>fruits, whole grains, and fish</span><i class="dot"></i></li>
    <li><span>Stop smoking cigarettes or chewing tobacco</span><i class="dot"></i></li>
    <li><span>Get help managing your high blood pressure,<br>diabetes, or to lose extra weight</span><i class="dot"></i></li>
    <li><span>Talk to your doctor about how you feel because your<br>mental health can affect your brain and physical health</span><i class="dot"></i></li>
    <li><span>If it is hard for you to get through the day because<br>of forgetfulness or memory problems, see your<br>doctor right away</span><i class="dot"></i></li>
  </ul>
  <p class="closing">You can do these things today to protect your mind and reduce<br>the risk of or slow down dementia.</p>

  <footer class="foot foot--front"><p>For more information about our project, please visit <b>https://novelmarrow.org/wellness-path/</b></p></footer>
</section>

<section class="page page--back" aria-label="Flyer page two">
  <div class="portrait portrait--top" role="img" aria-label="Photo of a smiling elder woman with glasses and earrings"></div>
  <div class="portrait portrait--mid" role="img" aria-label="Photo of a smiling woman with dark hair"></div>
  <div class="portrait portrait--low" role="img" aria-label="Photo of an elder man with glasses in a blue shirt"></div>

  <h2 class="back-title">The River of Life Flows Through Your Heart<br>to Protect Your Mind and Body</h2>
  <div class="back-rule"></div>
  <div class="back-intro">
    <p>Your heart health plays a big part in the health of your brain. Your heart is like the start of a flowing river. Blood vessels that take blood to and from your heart are like connected streams that flow through your body. They feed your brain with oxygen and energy.</p>
    <p>You can do things to keep the streams freely flowing through your body, so your heart and brain stay strong and healthy.</p>
  </div>

  <div class="ribbon">WORKING WITH YOUR DOCTOR</div>
  <ul class="doctor-steps">
    <li><svg class="step-icon" viewBox="0 0 20 20"><circle cx="10" cy="10" r="9" fill="#c98b83"/><circle cx="10" cy="10" r="5" fill="none" stroke="#fff" stroke-width="1.4"/><path d="M10 7v3.3l2 1.2" stroke="#fff" stroke-width="1.3" fill="none"/></svg>
      <p class="lead"><b>Make an appointment</b> for a “wellness” checkup with your<br>doctor every year</p>
      <ul><li>You will get tests and screenings to make sure you are healthy</li><li>They are usually free with Senior Care Plan B or the Tribal Wellness Service</li><li>If you have concerns about your memory, talk to your doctor</li></ul></li>
    <li><svg class="step-icon" viewBox="0 0 20 20"><circle cx="10" cy="10" r="9" fill="#c98b83"/><path d="M10 4.5c2.5 3.3 3.8 5.2 3.8 7a3.8 3.8 0 0 1-7.6 0c0-1.8 1.3-3.7 3.8-7z" fill="#fff"/></svg>
      <p class="lead"><b>Have your blood pressure checked</b> and know your<br>numbers</p>
      <ul><li>Your blood pressure should be less than 120/80 mmHg (120 over 80)</li><li>If you do not know how to take your blood pressure, ask your<br>&nbsp;&nbsp;doctor to show you</li></ul></li>
    <li><svg class="step-icon" viewBox="0 0 20 20"><circle cx="10" cy="10" r="9" fill="#c98b83"/><circle cx="10" cy="7" r="2.3" fill="#fff"/><path d="M5.8 15c.5-3 2-4.5 4.2-4.5s3.7 1.5 4.2 4.5z" fill="#fff"/></svg>
      <p class="lead"><b>Have your weight checked</b> regularly and know your number.<br>&nbsp;If you need to lose extra weight, ask your doctor about:</p>
      <ul><li>The right number of calories for your body</li><li>Ideas for healthier food choices</li><li>Support for losing weight</li></ul></li>
    <li><svg class="step-icon" viewBox="0 0 20 20"><circle cx="10" cy="10" r="9" fill="#c98b83"/><rect x="4.5" y="10" width="11" height="2.4" fill="#fff"/><path d="M13 8.5c0-1.5-1.5-1.5-1.5-3" stroke="#fff" fill="none"/></svg>
      <p class="lead"><b>If you smoke cigarettes or chew tobacco,</b> ask about medicine,<br>counseling, or help to stop</p></li>
    <li><svg class="step-icon" viewBox="0 0 20 20"><circle cx="10" cy="10" r="9" fill="#c98b83"/><path d="M10 15s-5-3-5-6.2A2.6 2.6 0 0 1 10 7.3a2.6 2.6 0 0 1 5 1.5C15 12 10 15 10 15z" fill="#fff"/></svg>
      <p><span class="lead"><b>If you do not have diabetes,</b> have your blood sugar level checked<br>during your visit.</span> Your blood sugar should be less than 100 mg/dL<br>when you have not eaten.</p></li>
    <li><svg class="step-icon" viewBox="0 0 20 20"><circle cx="10" cy="10" r="9" fill="#c98b83"/><path d="M5 6h10v6H9l-3 2.5V12H5z" fill="#fff"/></svg>
      <p><span class="lead"><b>Talk with your doctor</b> about all the medicines and vitamins you take.</span><br>Your doctor can make sure they do not cause any problems with your<br>memory, sleep, or brain function.</p></li>
  </ul>

  <div class="pill pill--other">OTHER STEPS YOU CAN TAKE</div>
  <ul class="other-steps">
    <li>Aim for 20 minutes of physical activity a day or 2 1/2 hours a week</li>
    <li>Eat less salt, sugar, red meat, and highly processed or packaged foods</li>
    <li>Read food labels to see how much salt (sodium) or fat is in your food</li>
    <li>Manage extra weight by making small changes. Losing a few pounds<br>makes a difference</li>
    <li>Limit alcohol. No more than 1 drink per day for women and 2 for men</li>
    <li>Take your medicine for blood pressure, diabetes, and other problems<br>even if you feel good</li>
    <li>Get at least seven hours of sleep each night. Talk to your doctor if you<br>have trouble sleeping</li>
    <li>Keep your mind active. Visit with people in your community, help plan tribal events,<br>go to your senior center, teach your language, play cards, or start a new hobby.</li>
  </ul>

  <div class="org"><span class="org__mark"></span><span class="org__name">NORTHWIND ELDERS ALLIANCE</span></div>

  <footer class="foot foot--back"><p>This product is supported by the National Office for Community Health (NOCH) of the Federal Department of Public Wellness (FDPW) as part of a financial assistance award totaling $348,711 with 100 percent funded by NOCH/FDPW. The contents are those of the author(s) and do not necessarily represent the official views of, nor an endorsement, by NOCH/FDPW, or the Government.</p></footer>
</section>

</body>
</html>
```